Website for Plumbing Company, Sir FlowBoiler

I need a 7-page fully HTML-coded website for my plumbing company, Sir FlowBoiler. We specialize in installation, repair, and replacement of both gas and electric water heaters. Although we offer both tankless (on-demand) water heaters and standard (with tank) water heaters, most of our business is related to standard (with tank) water heaters in the USA market.

These are the pages I need:
1. Home page with sections such as About Us, Our Services, Why Choose Us, Testimonials, Location Map (Palm Beach County Florida), Quote Request Form, Join Our Newsletter, Mission Statement, etc.

2. Gas Water Heaters

3. Electric Water Heaters

4. Tankless Water Heaters

5. About Us

6. Contact Us

7. Privacy Policy, Terms & Conditions

Be sure to mention the following points:
1. Same-Day Service
2. Best Price Guarantee
3. 100% Satisfaction Rating
4. 15-Year Warranty on Water Heater & Parts
5. Lifetime Warranty on Workmanship
*All Warranties are Transferrable Upon Home Sale

Once design is selected and finalized, I need the website coded in a standard HTML/CSS and temporarily hosted on your development server so I can see the website functionality that is not observable from screenshots, such as section animations, etc. Once those details are finalized, I will move the source code to my server and complete the project.

Target Market(s)

Residential Home Owners and Business Owners

Industry/Entity Type

Plumbing, Home Services, Remodeling, Construction

Coding

Coded - Design and coding required

Number of Pages Required

5+ page

Colors
0054AA
0677BA
7BADD7
CADEEF
E8F1F8
FFC000
F8CF3A
FAE287
FDF2CF
FEFAEE
EE7325
F08F49
F5BC92
FAE3D3
FDF4ED

Requirements
Must have
• Clean, colorful, and professional

```html
<!DOCTYPE html>
<html lang="en">
<head>
<meta charset="utf-8">
<title>Sir FlowBoiler – Water Heater Services</title>
<link href="https://fonts.googleapis.com/css2?family=Lexend:wght@300;400;500;600;700&display=swap" rel="stylesheet">
<style>
:root{
  --blue-dark:#0054aa;
  --blue:#0677ba;
  --blue-bright:#1a8ad6;
  --blue-soft:#7badd7;
  --blue-pale:#e8f1f8;
  --orange:#ee7325;
  --orange-lt:#f08f49;
  --yellow:#ffc000;
  --ink:#111a2b;
  --grey:#8a8f98;
  --white:#fff;
}
*{box-sizing:border-box;margin:0;padding:0}
html,body{width:1200px;height:3206px;overflow:hidden}
body{font-family:"Lexend",sans-serif;color:var(--ink);background:var(--white);position:relative}
.abs{position:absolute}
a{color:inherit;text-decoration:none}

/* header */
.topbar{left:0;top:0;width:1200px;height:92px;background:#fff}
.navbar{left:0;top:92px;width:1200px;height:47px;background:linear-gradient(90deg,var(--blue-bright),var(--blue-dark))}
.brand{left:117px;top:38px;display:flex;align-items:center;gap:10px;z-index:5}
.brand-dot{width:46px;height:46px;border-radius:50%;background:var(--blue-dark)}
.brand-name{font-size:25px;font-weight:700;color:var(--blue-dark)}
.nav{left:384px;top:92px;height:47px;display:flex;align-items:center;color:#fff;font-size:13.5px}
.nav a{margin-right:28px}
.reviews{left:580px;top:24px;width:146px;text-align:center}
.stars{color:var(--yellow);font-size:17px;letter-spacing:3px}
.reviews p{font-size:11.5px;font-weight:500}
.reviews .hub{font-size:14px;font-weight:500;color:var(--blue)}
.divider{left:748px;top:10px;width:2px;height:72px;background:#ccc}
.phone-top{left:768px;top:28px;display:flex;gap:10px;align-items:center}
.phone-top small{display:block;font-size:12px}
.phone-top strong{font-size:21px;color:var(--blue);font-weight:600}
.badge{left:984px;top:30px;width:92px;height:116px;border-radius:46px;background:linear-gradient(180deg,var(--blue-bright),var(--blue-dark));border:4px solid #fff;display:flex;flex-direction:column;align-items:center;justify-content:center;color:#fff;font-weight:700;line-height:1;z-index:6}
.badge span{display:block}

/* hero */
.hero-bg{left:0;top:139px;width:1200px;height:540px;background:linear-gradient(100deg,#d5d6d8 0%,#bfc1c4 40%,#a7abb0 100%)}
.hero-box{left:118px;top:248px;width:447px;height:317px;background:rgba(255,255,255,.93);padding:20px 0 0 30px}
.hero-box h1{font-size:43px;line-height:52px;font-weight:700;color:var(--ink)}
.hero-box h1 em{font-style:normal;color:var(--blue-bright)}
.hero-sub{left:142px;top:434px;font-size:19px;color:var(--ink)}
.btn{display:inline-flex;align-items:center;gap:10px;border-radius:22px;color:#fff;font-size:16px;height:42px;padding:0 10px 0 18px}
.btn i{width:22px;height:22px;border-radius:50%;border:2px solid #fff;display:inline-flex;align-items:center;justify-content:center;font-style:normal;font-size:12px}
.btn-blue{background:linear-gradient(90deg,var(--blue-bright),var(--blue-dark))}
.btn-orange{background:linear-gradient(90deg,var(--yellow),var(--orange))}
.hero-btns{left:135px;top:482px;display:flex;gap:16px}
.hero-art{left:560px;top:200px;width:640px;height:390px;background:linear-gradient(120deg,#e9eef5,#b9cce4 50%,#c2463a 85%);border-radius:40px 0 0 40px;opacity:.85}
.wave{left:0;top:560px;width:1200px;height:130px}

/* services */
.sec-title{width:1200px;left:0;text-align:center;font-size:28px;font-weight:400;color:var(--blue)}
.svc-sub{left:0;top:790px;width:1200px;text-align:center;font-size:19px;font-weight:600;color:var(--blue-bright)}
.lead{left:300px;top:835px;width:600px;text-align:center;font-size:13px;line-height:17px;color:var(--grey)}
.card{top:934px;width:229px;height:265px;overflow:hidden}
.card-img{width:229px;height:208px}
.card-label{position:absolute;bottom:0;left:0;width:229px;height:57px;background:linear-gradient(180deg,var(--blue-bright),var(--blue-dark));color:#fff;font-weight:600;font-size:13.5px;text-align:center;padding-top:30px}
.card-icon{position:absolute;left:92px;top:187px;width:44px;height:44px;border-radius:50%;background:var(--blue-bright);border:3px solid #fff;display:flex;align-items:center;justify-content:center}
.card-feature{background:linear-gradient(180deg,var(--blue-bright),var(--blue-dark));color:#fff;text-align:center;padding:46px 18px 0;overflow:visible}
.card-feature h3{font-size:13.5px;font-weight:600;margin-bottom:14px}
.card-feature p{font-size:12px;line-height:17.5px}
.card-feature .top-icon{position:absolute;left:92px;top:-22px;width:44px;height:44px;border-radius:50%;background:var(--blue-bright);border:3px solid #fff}

/* why */
.why-list{left:119px;top:1275px;width:452px;height:347px;background:linear-gradient(180deg,var(--blue-bright),var(--blue-dark))}
.why-row{height:56px;display:flex;align-items:center;gap:20px;padding-left:22px;color:#fff;font-size:16.5px;border-bottom:1px solid rgba(255,255,255,.25)}
.why-row svg{flex:none}
.why-note{position:absolute;left:0;bottom:0;width:452px;height:54px;background:var(--blue-bright);color:#fff;font-size:13px;text-align:center;line-height:54px}
.why-copy{left:628px;top:1270px;width:455px}
.why-copy h4{font-size:28px;font-weight:400;color:var(--blue)}
.why-copy h2{font-size:35px;font-weight:700;line-height:41px;margin:10px 0 20px}
.why-copy p.txt{font-size:13px;line-height:19px;color:var(--grey)}
.feat{display:flex;gap:22px;margin-top:30px}
.feat h5{font-size:13.5px;font-weight:600;margin-bottom:6px}
.feat p{font-size:13px;line-height:19px;color:var(--grey)}

/* process */
.step{width:240px;height:242px;background:linear-gradient(180deg,#fff,#ececee);text-align:center;padding:30px 20px 0}
.step h3{font-size:13.5px;font-weight:600;margin-bottom:14px}
.step p{font-size:12.5px;line-height:17.5px;color:var(--grey)}
.step-a{top:1755px;border:3px solid var(--blue);border-bottom:none;border-radius:12px 12px 0 0}
.step-b{top:1786px;border:3px solid var(--blue);border-top:none;border-radius:0 0 12px 12px;padding-top:68px}
.step-icon{width:72px;height:72px;border-radius:50%;background:linear-gradient(180deg,var(--blue-bright),var(--blue-dark));display:flex;align-items:center;justify-content:center;border:4px solid #fff}

/* testimonials */
.testi-bg{left:0;top:2108px;width:1200px;height:560px;background:linear-gradient(90deg,var(--blue-bright),var(--blue-dark))}
.testi-title{left:0;top:2134px;width:1200px;text-align:center;color:#fff;font-size:28px;font-weight:400}
.mascot{left:82px;top:2140px;width:420px;height:500px;border-radius:48% 48% 30% 30%;background:radial-gradient(circle at 50% 40%,#e7ecf2,#c84a3c 55%,#224e93 80%);opacity:.9}
.review{left:627px;width:453px;height:107px;background:#fff;display:flex}
.review-photo{width:108px;height:107px;background:linear-gradient(180deg,#d9dfe6,#8d98a6)}
.review-body{padding:12px 12px 0 15px;flex:1}
.review-body h5{font-size:12.5px;font-weight:600}
.review-body h5 span{color:var(--yellow);letter-spacing:2px;margin-left:10px;font-size:11px}
.review-body small{display:block;font-size:10.5px;color:var(--blue);margin-bottom:8px}
.review-body p{font-size:12px;line-height:17px;color:var(--grey)}
.bottom-wave{left:0;top:2560px;width:1200px;height:120px}

/* cta */
.cta{left:119px;top:2738px;width:961px;height:175px;border-radius:10px;background:linear-gradient(90deg,var(--blue-bright),var(--blue-dark))}
.cta h2{position:absolute;left:26px;top:28px;font-size:43px;font-weight:400;color:#fff}
.cta-btns{position:absolute;left:27px;top:100px;display:flex;gap:18px}
.cta .btn{background:rgba(255,255,255,.18);height:40px}
.cta-person{left:892px;top:2668px;width:170px;height:245px;border-radius:80px 80px 0 0;background:linear-gradient(180deg,#e8c7a8 0%,#c84a3c 45%,#1f4f97 100%)}

/* footer */
.foot-brand{left:120px;top:3000px;display:flex;align-items:center;gap:10px}
.foot-about{left:120px;top:3104px;width:270px;font-size:13px;line-height:18px;color:var(--grey)}
.fcol{top:2963px}
.fcol h6{font-size:13px;font-weight:500;color:var(--blue-bright);margin-bottom:12px}
.fcol li{list-style:none;font-size:13px;color:var(--grey);height:25.5px;display:flex;align-items:center;gap:8px}
.fcol li b{width:4px;height:4px;border-radius:50%;background:var(--blue-bright)}
.fcol li i{width:13px;height:13px;border-radius:50%;background:var(--blue-bright);flex:none}
.socials{left:889px;top:3080px;display:flex;gap:23px}
.socials span{width:30px;height:30px;border-radius:50%;border:2px solid var(--blue-bright);display:block}
.footbar{left:0;top:3176px;width:1200px;height:30px;background:var(--blue-bright);color:#fff;font-size:13px;display:flex;justify-content:space-between;align-items:center;padding:0 120px}
</style>
</head>
<body>

<!-- Header -->
<div class="abs topbar"></div>
<div class="abs navbar"></div>
<div class="abs brand"><span class="brand-dot"></span><span class="brand-name">Sir FlowBoiler</span></div>
<nav class="abs nav"><a>Home</a><a>About Us</a><a>Our Services ⌄</a><a>Why Choose Us</a><a>Testimonials</a><a>Contact Us</a></nav>
<div class="abs reviews"><div class="stars">★★★★★</div><p>300+ 5 Star Reviews</p><div class="hub">ReviewHub</div></div>
<div class="abs divider"></div>
<div class="abs phone-top">
  <svg width="40" height="40" viewBox="0 0 40 40"><circle cx="20" cy="20" r="17" fill="none" stroke="#111a2b" stroke-width="2.5"/><text x="20" y="25" text-anchor="middle" font-family="Lexend" font-size="12" font-weight="700" fill="#111a2b">24</text></svg>
  <div><small>24/7 EmergencyService</small><strong>0100-555-0199</strong></div>
</div>
<div class="abs badge" role="img" aria-label="Same Day Service badge"><span style="font-size:18px">Same</span><span style="font-size:27px">Day</span><span style="font-size:16px">Service</span></div>

<!-- Hero -->
<div class="abs hero-bg" role="img" aria-label="Suburban street with houses in soft grey tones"></div>
<div class="abs hero-art" role="img" aria-label="Branded service van with a smiling technician in red shirt and blue overalls"></div>
<div class="abs hero-box"><h1>Reliable Water<br>Heater Services –<br><em>Same Day</em></h1></div>
<p class="abs hero-sub">Gas | ElectricTankless | Installation &amp; Repair</p>
<div class="abs hero-btns"><a class="btn btn-blue">Schedule Service <i>›</i></a><a class="btn btn-orange">Call Now <i>›</i></a></div>
<svg class="abs wave" viewBox="0 0 1200 130" preserveAspectRatio="none">
  <path d="M0 30 C300 110 700 110 1200 0 L1200 130 L0 130Z" fill="#fff"/>
  <path d="M0 25 C250 95 650 95 1200 5 L1200 15 C700 105 300 115 0 55Z" fill="#1a8ad6"/>
  <path d="M0 60 C300 120 700 110 1200 20 L1200 40 C700 125 300 130 0 80Z" fill="#0054aa"/>
</svg>

<!-- Services -->
<h2 class="abs sec-title" style="top:733px">Our Services</h2>
<p class="abs svc-sub">Fove Star Installation, Repair, And Replacement Of Both Gas And Electric Water Heaters</p>
<p class="abs lead">Lorem Ipsum is simply dummy text of the printing and typesetting industry. Lorem Ipsum has been the industry's standard dummy text ever since the 1500s, when an unknown printer took a galley of type and scrambled it to make a type specimen book.</p>

<div class="abs card" style="left:120px"><div class="card-img" role="img" aria-label="Plumber fitting a pipe under a sink" style="background:linear-gradient(135deg,#e6e2dc,#b79880)"></div><div class="card-label">Installation</div><div class="card-icon"><svg width="20" height="20" viewBox="0 0 20 20"><path d="M3 17 L17 3 M3 3 L17 17" stroke="#fff" stroke-width="2.5" stroke-linecap="round"/></svg></div></div>
<div class="abs card card-feature" style="left:364px"><span class="top-icon"></span><h3>Electric Water Heaters</h3><p>Lorem Ipsum is simply dummy text of the printing and typesetting industry. Lorem Ipsum has been the industry's standard dummy text ever since the 1500s, when an unknown printer took a galley of type and scrambled it to make a type specimen book.</p></div>
<div class="abs card" style="left:607px"><div class="card-img" role="img" aria-label="Tank water heater installed in a utility room" style="background:linear-gradient(135deg,#d8dade,#8f949b)"></div><div class="card-label">Gas Water Heaters</div><div class="card-icon"><svg width="16" height="20"><rect x="2" y="1" width="12" height="18" rx="4" fill="none" stroke="#fff" stroke-width="2"/></svg></div></div>
<div class="abs card" style="left:851px"><div class="card-img" role="img" aria-label="Technician repairing water heater fittings" style="background:linear-gradient(135deg,#dfe5ec,#6f8fb8)"></div><div class="card-label">Repair</div><div class="card-icon"><svg width="16" height="20"><rect x="2" y="1" width="12" height="18" rx="4" fill="none" stroke="#fff" stroke-width="2"/></svg></div></div>

<!-- Why choose -->
<div class="abs why-list">
  <div class="why-row"><svg width="34" height="34" viewBox="0 0 34 34"><circle cx="17" cy="17" r="13" fill="none" stroke="#fff" stroke-width="2.5"/><path d="M17 9 V17 L23 21" stroke="#fff" stroke-width="2.5" fill="none"/></svg>Same-Day Service</div>
  <div class="why-row"><svg width="34" height="34" viewBox="0 0 34 34"><circle cx="17" cy="13" r="10" fill="none" stroke="#fff" stroke-width="2.5"/><path d="M10 21 L6 32 M24 21 L28 32" stroke="#fff" stroke-width="2.5"/><text x="17" y="18" text-anchor="middle" font-size="13" fill="#fff" font-family="Lexend">$</text></svg>Best Price Guarantee</div>
  <div class="why-row"><svg width="34" height="34" viewBox="0 0 34 34"><circle cx="17" cy="17" r="10" fill="#fff"/><path d="M17 2 V7 M17 27 V32 M2 17 H7 M27 17 H32 M6 6 L10 10 M24 24 L28 28 M28 6 L24 10 M6 28 L10 24" stroke="#fff" stroke-width="2.5"/></svg>100% Satisfaction Rating</div>
  <div class="why-row"><svg width="34" height="34" viewBox="0 0 34 34"><circle cx="17" cy="17" r="13" fill="#fff"/><path d="M11 17 L15 21 L23 13" stroke="#0677ba" stroke-width="3" fill="none"/></svg>15-Year Warranty on Water Heater &amp; Parts</div>
  <div class="why-row"><svg width="34" height="34" viewBox="0 0 34 34"><path d="M17 3 L29 8 V17 C29 24 23 29 17 31 C11 29 5 24 5 17 V8Z" fill="#fff"/></svg>Lifetime Warranty on Workmanship</div>
  <div class="why-note">*All Warranties are Transferrable Upon Home Sale</div>
</div>
<div class="abs why-copy">
  <h4>Why Choose Us</h4>
  <h2>Lorem Ipsum is simply dummy text</h2>
  <p class="txt">Lorem Ipsum is simply dummy text of the printing and typesetting industry lorem Ipsum has been the industry's dummy text.</p>
  <div class="feat"><svg width="56" height="56" viewBox="0 0 56 56" style="flex:none"><circle cx="28" cy="28" r="26" fill="#ee7325"/><circle cx="28" cy="28" r="17" fill="none" stroke="#fff" stroke-width="2.5"/><path d="M20 28 L26 34 L36 22" stroke="#fff" stroke-width="3" fill="none"/></svg><div><h5>Certified Technicians &amp; Honest Pricing</h5><p>Lorem Ipsum is simply dummy text of the printing and typesetting industry.</p></div></div>
  <div class="feat"><svg width="56" height="62" viewBox="0 0 56 62" style="flex:none"><path d="M28 2 L52 10 V30 C52 46 40 56 28 60 C16 56 4 46 4 30 V10Z" fill="#f08f49"/></svg><div><h5>Industry-Leading Warranties</h5><p>Lorem Ipsum is simply dummy text of the printing and typesetting industry.</p></div></div>
</div>

<!-- Process -->
<h2 class="abs sec-title" style="top:1688px">Our Process</h2>
<div class="abs step step-a" style="left:120px"><h3>Contact Us</h3><p>Lorem Ipsum is simply dummy text of the printing and typesetting industry. Lorem Ipsum has been the industry's standard dummy text ever since the 1500.</p></div>
<div class="abs step-icon" style="left:204px;top:1956px"><svg width="34" height="34" viewBox="0 0 24 24"><path d="M6.6 10.8a15 15 0 0 0 6.6 6.6l2.2-2.2c.3-.3.7-.4 1-.2 1.1.4 2.3.6 3.6.6.6 0 1 .4 1 1V20c0 .6-.4 1-1 1A17 17 0 0 1 3 4c0-.6.4-1 1-1h3.5c.6 0 1 .4 1 1 0 1.3.2 2.5.6 3.6.1.3 0 .7-.2 1z" fill="#fff"/></svg></div>
<div class="abs step step-b" style="left:361px"><h3>Same-Day Inspection</h3><p>Lorem Ipsum is simply dummy text of the printing and typesetting industry. Lorem Ipsum has been the industry's standard dummy text ever since the 1500.</p></div>
<div class="abs step-icon" style="left:444px;top:1752px"><svg width="34" height="34" viewBox="0 0 34 34"><circle cx="20" cy="14" r="9" fill="none" stroke="#fff" stroke-width="2.5"/><path d="M13 21 L5 29" stroke="#fff" stroke-width="3"/><path d="M16 14 L19 17 L24 11" stroke="#fff" stroke-width="2" fill="none"/></svg></div>
<div class="abs step step-a" style="left:600px"><h3>Installation / Repair</h3><p>Lorem Ipsum is simply dummy text of the printing and typesetting industry. Lorem Ipsum has been the industry's standard dummy text ever since the 1500.</p></div>
<div class="abs step-icon" style="left:684px;top:1956px"><svg width="34" height="34" viewBox="0 0 34 34"><path d="M6 28 L28 6 M6 6 L28 28" stroke="#fff" stroke-width="3.5" stroke-linecap="round"/></svg></div>
<div class="abs step step-b" style="left:841px"><h3>Guaranteed Satisfaction</h3><p>Lorem Ipsum is simply dummy text of the printing and typesetting industry. Lorem Ipsum has been the industry's standard dummy text ever since the 1500.</p></div>
<div class="abs step-icon" style="left:924px;top:1752px"><svg width="34" height="34" viewBox="0 0 34 34"><path d="M17 3 L29 8 V17 C29 24 23 29 17 31 C11 29 5 24 5 17 V8Z" fill="#fff"/></svg></div>

<!-- Testimonials -->
<div class="abs testi-bg"></div>
<h2 class="abs testi-title">Testimonials</h2>
<div class="abs mascot" role="img" aria-label="Cartoon plumber mascot carrying a water heater tank on his shoulder"></div>
<div class="abs review" style="top:2208px"><div class="review-photo" role="img" aria-label="Portrait of a smiling customer"></div><div class="review-body"><h5>Marla Quinton<span>★★★★★</span></h5><small>Designation Here</small><p>"Lorem Ipsum is simply dummy text of the printing and typesetting industry."</p></div></div>
<div class="abs review" style="top:2340px"><div class="review-photo" role="img" aria-label="Portrait of a customer in a suit"></div><div class="review-body"><h5>Devin Ashcroft<span>★★★★★</span></h5><small>Designation Here</small><p>"Lorem Ipsum is simply dummy text of the printing and typesetting industry."</p></div></div>
<div class="abs review" style="top:2472px"><div class="review-photo" role="img" aria-label="Portrait of a customer in a blue shirt"></div><div class="review-body"><h5>Theo Barrick<span>★★★★★</span></h5><small>Designation Here</small><p>"Lorem Ipsum is simply dummy text of the printing and typesetting industry."</p></div></div>
<svg class="abs bottom-wave" viewBox="0 0 1200 120" preserveAspectRatio="none">
  <path d="M0 40 C400 100 800 0 1200 100 L1200 120 L0 120Z" fill="#fff"/>
  <path d="M0 35 C400 95 800 -5 1200 95 L1200 105 C800 5 400 105 0 55Z" fill="#7badd7"/>
</svg>

<!-- CTA -->
<div class="abs cta">
  <h2>Need Hot Water Today?</h2>
  <div class="cta-btns"><a class="btn">Schedule Same-Day Service <i>›</i></a><a class="btn">Call Now <i>›</i></a></div>
</div>
<div class="abs cta-person" role="img" aria-label="Technician in red shirt and blue overalls with arms crossed"></div>

<!-- Footer -->
<div class="abs foot-brand"><span class="brand-dot"></span><span class="brand-name">Sir FlowBoiler</span></div>
<p class="abs foot-about">Lorem Ipsum is simply dummy text of the printing and typesetting industry.</p>
<div class="abs fcol" style="left:428px"><h6>Quick Links</h6><ul><li><b></b>Home</li><li><b></b>About Us</li><li><b></b>Our Services</li><li><b></b>Why Choose Us</li><li><b></b>Testimonials</li><li><b></b>Contact Us</li></ul></div>
<div class="abs fcol" style="left:598px"><h6>Trust Badges</h6><ul><li><i></i>Same-Day Service</li><li><i></i>Best Price Guarantee</li><li><i></i>100% Satisfaction Rating</li><li><i></i>15-Year Warranty</li><li><i></i>Lifetime Workmanship Warranty</li><li><i></i>*Transferable Upon Home Sale</li></ul></div>
<div class="abs fcol" style="left:889px"><h6>Contact Us</h6><ul>
  <li><svg width="12" height="12" viewBox="0 0 24 24"><path d="M6.6 10.8a15 15 0 0 0 6.6 6.6l2.2-2.2c.3-.3.7-.4 1-.2 1.1.4 2.3.6 3.6.6.6 0 1 .4 1 1V20c0 .6-.4 1-1 1A17 17 0 0 1 3 4c0-.6.4-1 1-1h3.5c.6 0 1 .4 1 1 0 1.3.2 2.5.6 3.6.1.3 0 .7-.2 1z" fill="#1a8ad6"/></svg>0100-555-0199</li>
  <li style="height:20px"><svg width="12" height="10" viewBox="0 0 12 10"><rect x="0.5" y="0.5" width="11" height="9" fill="#1a8ad6"/><path d="M0.5 0.5 L6 5 L11.5 0.5" stroke="#fff" fill="none"/></svg>info@sirflowboiler.com</li>
  <li style="align-items:flex-start;height:auto;line-height:16px;margin-top:4px"><svg width="12" height="14" viewBox="0 0 12 14" style="margin-top:2px"><path d="M6 0 A5 5 0 0 1 11 5 C11 9 6 14 6 14 C6 14 1 9 1 5 A5 5 0 0 1 6 0Z" fill="#1a8ad6"/><circle cx="6" cy="5" r="2" fill="#fff"/></svg>Sample Lane 7B,<br>Block-400210</li>
</ul></div>
<div class="abs socials"><span></span><span></span><span></span><span></span></div>
<div class="abs footbar"><span>© SirFlowBoiler 2026. All Rights Reserved</span><span>Privacy Policy | Terms &amp; Conditions</span></div>

</body>
</html>
```